New Flyer Design Project for phone case sales website

we need a double sided flyer to include with orders from one business to promote another new new business. These flyers are to promote our new business that sells mobile phone cases for Velmora and Orbix models. The url for the new site is www.quillowdrift.co.uk.

Target Market(s)

Anybody with a phone

Requirements
Must have
• I like the idea to have the back of the flyer portrait with a black background. I would like the outline of any velmora or orbix with our logo in the middle. I would also like our url underneath this. Can we have the wording on the front something like.
Thank you very much for your order on Fern Quay. We have teamed up with Fern Quay to offer a 10% discount on any order placed on our website. We offer phone cases to suit all Orbix and Velmora models. Why don't you check out our range? Simply enter FERNQUAY during checkout to apply your discount.
Nice to have
• Although the back will be black, the front does not necessarily need to be.

Flyer size is A6.

```html
<!DOCTYPE html>
<html lang="en">
<head>
<meta charset="utf-8">
<title>Quillow Drift – Flyer Front and Back</title>
<link href="https://fonts.googleapis.com/css2?family=Bebas+Neue&family=Lato:ital,wght@0,400;0,700;1,400&family=Montserrat:wght@600;700&display=swap" rel="stylesheet">
<style>
  :root{
    --stage:#5f5d5e;
    --paper:#ffffff;
    --ink:#1d1d1b;
    --grey-text:#6b6b6b;
    --red:#c62127;
    --orange:#e8782a;
    --yellow:#f5c518;
    --blue:#29a9e0;
    --sky-link:#1fa3de;
    --black:#000000;
    --outline-grey:#2a2a2a;
  }
  *{margin:0;padding:0;box-sizing:border-box}
  html,body{width:1200px;height:1200px;overflow:hidden;background:var(--stage)}
  .canvas{position:relative;width:1200px;height:1200px}

  /* FRONT */
  .flyer-front{position:absolute;left:43px;top:269px;width:466px;height:598px;background:var(--paper);overflow:hidden;box-shadow:0 6px 18px rgba(0,0,0,.35)}
  .front-shapes{position:absolute;inset:0}
  .brand-lockup{position:absolute;left:0;right:0;top:70px;display:flex;justify-content:center;align-items:center;gap:7px}
  .brand-square{width:11px;height:11px;background:var(--red)}
  .brand-name{font-family:'Montserrat',sans-serif;font-weight:600;font-size:14px;letter-spacing:.6px;color:var(--grey-text)}
  .headline{position:absolute;left:14px;top:186px;color:var(--paper)}
  .headline-main{font-family:'Bebas Neue',sans-serif;font-size:31px;line-height:30px;letter-spacing:.3px}
  .headline-sub{font-family:'Lato',sans-serif;font-size:25px;line-height:25px}
  .headline-rule{width:87px;height:2px;background:var(--paper);margin-top:6px}
  .body-copy{position:absolute;left:14px;top:384px;width:205px;font-family:'Lato',sans-serif;font-size:10px;line-height:13.2px;color:var(--ink)}
  .body-copy p{margin-bottom:6px}
  .body-copy .highlight{color:var(--sky-link);font-weight:700}
  .body-copy .prompt{color:var(--red);font-style:italic;margin-bottom:0}
  .discount{position:absolute;left:272px;top:420px;width:120px;text-align:center;color:var(--paper)}
  .discount-figure{font-family:'Bebas Neue',sans-serif;font-size:44px;line-height:38px}
  .discount-word{font-family:'Bebas Neue',sans-serif;font-size:28px;line-height:24px}
  .discount-note{font-family:'Lato',sans-serif;font-size:7px;margin-top:2px}
  .model-row{position:absolute;left:29px;top:527px;display:flex;align-items:center;gap:12px;font-family:'Lato',sans-serif;font-weight:700;font-size:9px;color:var(--ink)}
  .model-divider{width:1px;height:22px;background:var(--ink)}
  .front-footer{position:absolute;left:0;right:0;bottom:0;height:39px;background:var(--red);display:flex;align-items:center;justify-content:center;font-family:'Lato',sans-serif;font-size:10px;letter-spacing:1.4px;color:var(--paper)}

  /* BACK */
  .flyer-back{position:absolute;left:528px;top:363px;width:643px;height:499px;background:var(--black);box-shadow:0 6px 18px rgba(0,0,0,.35)}
  .phone-outline{position:absolute;top:139px;width:115px;height:230px;border:1.5px solid #d9d9d9;border-radius:16px;background:var(--outline-grey)}
  .phone-outline.left{left:80px}
  .phone-outline.right{left:449px}
  .back-lockup{position:absolute;left:245px;top:229px;width:152px;height:75px;border-top:1px solid #333;border-bottom:1px solid #333;display:flex;align-items:flex-end;justify-content:center;gap:6px;padding-bottom:6px}
  .back-lockup .brand-square{width:12px;height:12px;margin-bottom:3px}
  .back-lockup .brand-name{color:var(--paper);font-weight:700;font-size:14px}
  .back-url{position:absolute;left:0;right:0;top:448px;text-align:center;font-family:'Lato',sans-serif;font-size:14px;letter-spacing:3px;color:var(--paper)}
</style>
</head>
<body>
<div class="canvas">

  <section class="flyer-front">
    <svg class="front-shapes" width="466" height="598" viewBox="0 0 466 598">
      <polygon points="0,85 225,112 466,79 466,318 0,365" fill="var(--yellow)"/>
      <rect x="-20" y="159" width="163" height="152" rx="22" fill="var(--orange)"/>
      <rect x="-20" y="178" width="257" height="114" rx="22" fill="var(--red)"/>
      <defs>
        <linearGradient id="caseTone" x1="0" y1="0" x2="1" y2="1">
          <stop offset="0" stop-color="#5b84d6"/>
          <stop offset=".6" stop-color="#4568c0"/>
          <stop offset="1" stop-color="#b0407f"/>
        </linearGradient>
      </defs>
      <rect x="200" y="113" width="290" height="276" rx="18" fill="url(#caseTone)" role="img" aria-label="Product photo of a blue ring-holder phone case with a phone"/>
      <circle cx="292" cy="427" r="40" fill="var(--orange)"/>
      <circle cx="379" cy="477" r="47" fill="var(--blue)"/>
      <circle cx="267" cy="489" r="17" fill="var(--blue)"/>
      <circle cx="332" cy="464" r="73" fill="var(--red)"/>
      <circle cx="388" cy="400" r="10" fill="var(--blue)"/>
      <circle cx="300" cy="415" r="8" fill="var(--blue)"/>
      <circle cx="299" cy="522" r="18" fill="var(--yellow)"/>
      <circle cx="371" cy="506" r="6" fill="var(--yellow)"/>
      <circle cx="351" cy="511" r="3" fill="var(--yellow)"/>
    </svg>

    <div class="brand-lockup"><span class="brand-square"></span><span class="brand-name">QUILLOW DRIFT</span></div>

    <h1 class="headline">
      <div class="headline-main">MOBILE PHONE CASES</div>
      <div class="headline-sub">for Velmora and<br>Orbix models.</div>
      <div class="headline-rule"></div>
    </h1>

    <div class="body-copy">
      <p>Thank you very much for your order on Fern Quay. We have teamed up with Fern Quay to offer a <span class="highlight">10% discount</span> on any order placed on our website.</p>
      <p>We offer phone cases to suit all Orbix and Velmora models.</p>
      <p class="prompt">Why don't you check out our range?</p>
      <p>Simply enter FERNQUAY during checkout to apply your discount.</p>
    </div>

    <div class="discount">
      <div class="discount-figure">10%</div>
      <div class="discount-word">DISCOUNT</div>
      <div class="discount-note">on any order placed on website</div>
    </div>

    <div class="model-row"><span>Orbix</span><span class="model-divider"></span><span>Velmora</span></div>

    <footer class="front-footer">www.quillowdrift.co.uk</footer>
  </section>

  <section class="flyer-back">
    <div class="phone-outline left" role="img" aria-label="Line drawing of a full-screen phone"></div>
    <div class="back-lockup"><span class="brand-square"></span><span class="brand-name">QUILLOW DRIFT</span></div>
    <div class="phone-outline right" role="img" aria-label="Line drawing of a phone with home button"></div>
    <div class="back-url">www.quillowdrift.co.uk</div>
  </section>

</div>
</body>
</html>
```